Career Management Consultant Fun Professional Business Card

This is a business card for a personal career management consultant. The vibe needs to be professional but fun, modern with colour.

The name of the business is "Marcus Telvorne Career Management Consulting"

The name of the individual is "Marcus Telvorne" and his title is "Career Management Consultant"

Contact Information for Business Card

Marcus Telvorne
Phone: 0400 731 862
Email: Marcus.Telvorne@quillmail.net

```html
<!DOCTYPE html>
<html lang="en">
<head>
<meta charset="utf-8">
<title>Marcus Telvorne — Business Card</title>
<link rel="stylesheet" href="https://fonts.googleapis.com/css2?family=Marcellus+SC&family=Quicksand:wght@400&display=swap">
<style>
  :root {
    --backdrop: #e9e9e9;
    --card-light: #f4f4f4;
    --card-mid: #e2e2e2;
    --card-shade: #d6d6d6;
    --ink: #2b2b2b;
    --ink-soft: #5a5a5a;
    --accent: #d8232a;
    --mark: #1c1c1c;
  }
  * { box-sizing: border-box; margin: 0; padding: 0; }
  html, body {
    width: 1200px; height: 873px; overflow: hidden;
    background: var(--backdrop);
  }
  .canvas {
    position: relative; width: 1200px; height: 873px;
    display: flex; align-items: center; justify-content: center; gap: 60px;
  }
  .card {
    position: relative; width: 525px; height: 300px;
    box-shadow: 0 6px 18px rgba(0,0,0,0.12);
    overflow: hidden;
  }
  .card-texture {
    position: absolute; inset: 0;
    background:
      linear-gradient(180deg, rgba(255,255,255,0.5) 0%, rgba(255,255,255,0) 30%, rgba(200,200,200,0.25) 55%, rgba(255,255,255,0.3) 80%),
      linear-gradient(90deg, var(--card-light) 0%, var(--card-mid) 45%, var(--card-shade) 65%, var(--card-light) 100%);
  }
  .identity {
    position: absolute; display: flex; align-items: flex-start; gap: 12px;
  }
  .mark-square {
    flex: none; background: var(--mark);
  }
  .details { display: flex; flex-direction: column; }
  .name {
    font-family: "Marcellus SC", serif; color: var(--ink);
    letter-spacing: 0.06em; line-height: 1;
  }
  /* Front: contact side */
  .card-front .identity { left: 150px; top: 96px; }
  .card-front .mark-square { width: 46px; height: 46px; }
  .card-front .name { font-size: 20px; margin-top: 24px; }
  .contact-list {
    list-style: none; margin-top: 6px;
    font-family: "Quicksand", sans-serif; font-size: 16px; color: var(--ink-soft);
    line-height: 1.35;
    border-bottom: 2px solid var(--accent); padding-bottom: 3px;
  }
  .contact-label { color: var(--accent); margin-right: 4px; }
  /* Back: brand side */
  .card-back .identity { left: 140px; top: 92px; gap: 10px; }
  .card-back .mark-square { width: 42px; height: 42px; }
  .card-back .name { font-size: 27px; margin-top: 20px; }
  .tagline {
    font-family: "Marcellus SC", serif; font-size: 13px; color: var(--ink-soft);
    letter-spacing: 0.08em; margin-top: 6px; padding-bottom: 3px;
    border-bottom: 2px solid var(--accent);
  }
</style>
</head>
<body>
<main class="canvas">
  <section class="card card-front" aria-label="Business card front">
    <div class="card-texture" role="img" aria-label="Whitewashed wood grain texture"></div>
    <div class="identity">
      <span class="mark-square" aria-hidden="true"></span>
      <div class="details">
        <p class="name">Marcus Telvorne</p>
        <ul class="contact-list">
          <li><span class="contact-label">P</span>0400 731 862</li>
          <li><span class="contact-label">E</span>Marcus.Telvorne@quillmail.net</li>
        </ul>
      </div>
    </div>
  </section>
  <section class="card card-back" aria-label="Business card back">
    <div class="card-texture" role="img" aria-label="Whitewashed wood grain texture"></div>
    <div class="identity">
      <span class="mark-square" aria-hidden="true"></span>
      <div class="details">
        <p class="name">Marcus Telvorne</p>
        <p class="tagline">Career Management Consulting</p>
      </div>
    </div>
  </section>
</main>
</body>
</html>
```